New ecommerce website needed for Epoxy Retailer

We need a new shopify website designed and built for our epoxy supply store.
We sell Epoxy, wood, epoxy furniture, supplies and provide classes on how to use epoxy.
We are looking for a website with a home page and 7 primary navigation links at the top. Some of these links should have a drop down menu with the below listed pages linked to them...
Sub Pages:
- Brindle Epoxy
- Epoxy
- Pigments
- Marten Oil
- Molds
- Silicone
- HDPE
- Wood
- Live Edge
- Ovals & Rounds
- Pre-cut
- Charcuterie Wood
- Custom Milling
- Wholesale
- Supplies
- Furniture
-Education
- In person workshops
- My courses (are we able to have a login section for customers to see their purchases?)
- About Us

```html
<!DOCTYPE html>
<html lang="en">
<head>
<meta charset="utf-8">
<title>Oakmere Studio — Epoxy Furniture and Supplies</title>
<link href="https://fonts.googleapis.com/css2?family=Jost:wght@300;400;500&display=swap" rel="stylesheet">
<style>
:root{
  --bg:#262222;
  --bg-footer:#2e2a2a;
  --bg-bar:#1c1919;
  --panel:rgba(66,64,64,.92);
  --text:#ffffff;
  --muted:#d8d4d2;
  --dark:#1f1c1c;
  --line:rgba(255,255,255,.55);
}
*{box-sizing:border-box;margin:0;padding:0}
html,body{width:1200px;height:5142px;overflow:hidden}
body{background:var(--bg);color:var(--text);font-family:'Jost',sans-serif;position:relative}
.abs{position:absolute}
.photo{position:absolute}
.btn{position:absolute;display:flex;align-items:center;justify-content:center;font-size:10px;letter-spacing:3px;text-transform:uppercase;border-radius:4px}
.btn-dark{background:var(--dark);color:var(--text);border:1px solid #555}
.btn-light{background:#fff;color:var(--dark)}
.btn-outline{border:1px solid var(--line);color:var(--text)}
h1,h2{font-weight:400;text-transform:uppercase;letter-spacing:-.5px}
.para{font-size:12px;line-height:19px;font-weight:300;color:var(--muted)}
.para-rule{border-left:2px solid #fff;padding-left:12px}

/* header */
.hero{left:0;top:0;width:1200px;height:750px;
  background:
    radial-gradient(ellipse 260px 120px at 780px 470px,rgba(20,24,40,.95),rgba(20,24,40,0) 100%),
    radial-gradient(circle 40px at 30px 560px,rgba(255,255,255,.9),rgba(255,255,255,0)),
    radial-gradient(circle 40px at 1170px 590px,rgba(255,255,255,.9),rgba(255,255,255,0)),
    linear-gradient(180deg,#3e4443 0%,#5d6564 30%,#6f7877 55%,#aeb4b3 68%,#3a3f3f 84%,#242828 100%)}
.search{left:160px;top:8px;width:340px;height:18px;border-bottom:1px solid var(--line);font-size:9px;display:flex;align-items:center;justify-content:space-between;color:var(--muted)}
.nav{top:52px;font-size:11px;display:flex;gap:34px}
.brand-badge{left:540px;top:2px;width:120px;height:110px;border-radius:50%;background:var(--dark);border:3px solid #fff;display:flex;flex-direction:column;align-items:center;justify-content:center;font-size:13px;font-weight:500;letter-spacing:1px;line-height:16px;text-transform:uppercase}
.features{left:150px;top:640px;width:900px;height:220px;background:var(--panel);border-radius:12px;display:flex;justify-content:space-around;align-items:center;padding:0 30px}
.feature{display:flex;flex-direction:column;align-items:center;gap:18px;font-size:13px;text-transform:uppercase}
.feature i{width:80px;height:80px;border-radius:50%;background:#2b2828;display:flex;align-items:center;justify-content:center}

/* categories */
.section-title{left:0;width:1200px;text-align:center;font-size:40px}
.cat{position:absolute;border-radius:6px;overflow:hidden}
.cat .label{position:absolute;left:34px;bottom:30px;font-size:18px;text-transform:uppercase;border-left:2px solid #fff;padding-left:8px;line-height:20px}
.cat .go{position:absolute;right:16px;bottom:18px;width:40px;height:40px;border-radius:50%;background:#fff;display:flex;align-items:center;justify-content:center}

/* classes */
.class-card{left:102px;top:2472px;width:594px;height:334px;background:linear-gradient(135deg,#fafafa,#e4e4e4 50%,#f4f4f4);color:var(--dark);border-radius:6px}
.class-card h2{position:absolute;left:48px;top:38px;font-size:38px;line-height:48px}
.class-card .para{position:absolute;left:48px;top:160px;width:440px;color:#333;border-color:#333}

/* products */
.tabs{top:2970px;left:220px;display:flex;align-items:center;font-size:9px;letter-spacing:2px;text-transform:uppercase}
.tabs span{width:152px;text-align:center;border-right:1px solid var(--line);height:16px;line-height:16px}
.tabs .active{background:#fff;color:var(--dark);height:36px;line-height:36px;border-radius:4px;border:none}
.product{position:absolute;width:212px;text-align:center}
.product .photo{position:relative;height:254px;border-radius:4px;
  background:
    radial-gradient(ellipse 60px 26px at 118px 172px,rgba(38,130,150,.85),rgba(38,130,150,0)),
    radial-gradient(ellipse 70px 90px at 110px 130px,#d6dadd,rgba(214,218,221,0)),
    #ffffff}
.product .photo.warm{background:
    radial-gradient(ellipse 60px 26px at 118px 172px,rgba(196,104,48,.85),rgba(196,104,48,0)),
    radial-gradient(ellipse 70px 90px at 110px 130px,#d9dbdc,rgba(217,219,220,0)),
    #ffffff}
.product .name{font-size:11px;margin-top:18px}
.product .price{font-size:17px;letter-spacing:1px;margin-top:2px}
.product .btn{position:relative;height:28px;margin-top:10px;border-radius:3px;font-size:8px}

/* footer */
.footer{left:0;top:4680px;width:1200px;height:430px;background:var(--bg-footer)}
.footer-brand{left:150px;top:4740px;width:212px;height:200px;border-radius:50%;border:3px solid #fff;display:flex;flex-direction:column;align-items:center;justify-content:center;font-size:26px;font-weight:500;letter-spacing:2px;line-height:30px;text-transform:uppercase}
.foot-head{font-size:13px;text-transform:uppercase}
.foot-links{font-size:11px;line-height:30px}
.contact-row{display:flex;align-items:center;gap:14px;font-size:11px;line-height:15px}
.contact-row i{width:22px;height:22px;border-radius:50%;background:#fff;display:flex;align-items:center;justify-content:center;flex-shrink:0}
.vline{width:1px;background:rgba(255,255,255,.3)}
.copy{left:0;top:5110px;width:1200px;height:32px;background:var(--bg-bar);font-size:11px;display:flex;align-items:center;justify-content:center}
</style>
</head>
<body>

<!-- Header + hero -->
<div class="photo hero" role="img" aria-label="Dim concrete showroom with a dark sofa, pendant lamps and glowing floor lights"></div>
<div class="abs search"><span>What Are You Looking For?</span>
  <svg width="14" height="14" viewBox="0 0 14 14"><circle cx="7" cy="7" r="6.5" fill="#fff"/><circle cx="6.5" cy="6.5" r="2.5" fill="none" stroke="#333"/><line x1="8.3" y1="8.3" x2="10" y2="10" stroke="#333"/></svg>
</div>
<div class="abs" style="left:994px;top:6px;display:flex;gap:12px">
  <svg width="20" height="20"><circle cx="10" cy="10" r="10" fill="#fff"/><rect x="6" y="7" width="8" height="7" fill="none" stroke="#333"/></svg>
  <svg width="20" height="20"><circle cx="10" cy="10" r="10" fill="#fff"/><circle cx="10" cy="8" r="2.5" fill="none" stroke="#333"/><path d="M6 15a4 4 0 0 1 8 0" fill="none" stroke="#333"/></svg>
</div>
<nav class="abs nav" style="left:218px"><span>Home</span><span>Brindle Epoxy ▾</span><span>Molds ▾</span><span>Wood ▾</span></nav>
<div class="abs brand-badge">Oakmere<br><span style="font-size:9px;letter-spacing:3px">Studio</span></div>
<nav class="abs nav" style="left:710px"><span>Supplies ▾</span><span>Furniture ▾</span><span>Education ▾</span><span>About Us</span></nav>

<h1 class="abs" style="left:150px;top:170px;font-size:44px;line-height:55px">We Provide Best<br>Epoxy Furniture<br>And Supplies</h1>
<p class="abs para para-rule" style="left:160px;top:356px;width:470px;color:#eee">Lorem Ipsum is simply dummy text of the printing and typesetting industry. Lorem Ipsum has been the industry's standard dummy text ever since the 1500s, when an unknown printer took a galley of type and scrambled it to make a type specimen book.</p>
<div class="btn btn-dark" style="left:150px;top:468px;width:152px;height:36px">Shop Now</div>

<div class="abs features">
  <div class="feature"><i><svg width="40" height="40" fill="none" stroke="#fff" stroke-width="2"><path d="M6 28l20-18 8 4-20 18z"/><path d="M6 28v4l8 4 20-18v-4"/></svg></i>Solid Woods</div>
  <div class="feature"><i><svg width="40" height="40" fill="none" stroke="#fff" stroke-width="2"><path d="M8 14l6-7h12l6 7-12 18z"/><path d="M8 14h24"/></svg></i>Premium Epoxy</div>
  <div class="feature"><i><svg width="40" height="40" fill="none" stroke="#fff" stroke-width="2"><circle cx="20" cy="14" r="8"/><path d="M17 14l2 2 4-4"/><path d="M6 32h10l6-4h10"/></svg></i>Derdone Assure</div>
  <div class="feature"><i><svg width="40" height="40" fill="none" stroke="#fff" stroke-width="2"><path d="M6 14l10-6h18l-10 6z"/><path d="M6 14v14M24 14v14M34 8v14"/></svg></i>Custom Tables</div>
</div>

<!-- Categories -->
<h2 class="abs section-title" style="top:935px">Browse By Our Category</h2>
<p class="abs para" style="left:240px;top:1010px;width:720px;text-align:center">Lorem Ipsum is simply dummy text of the printing and typesetting industry. Lorem Ipsum has been the industry's standard dummy text ever since the 1500s, when an unknown printer took a galley of type and scrambled it to make a type specimen book.</p>

<div class="cat" style="left:150px;top:1100px;width:518px;height:310px;background:radial-gradient(ellipse 200px 70px at 300px 140px,#c06a22,rgba(192,106,34,0)),radial-gradient(ellipse 160px 60px at 120px 90px,#9a5220,rgba(154,82,32,0)),linear-gradient(170deg,#6b4e33 0%,#cfd7db 40%,#e7ecee 60%,#7e7a76 82%,#2a2826 100%)" role="img" aria-label="Live-edge wood table with clear epoxy river"><span class="label">Brindle Epoxy</span><span class="go"><svg width="18" height="10"><path d="M0 5h16M12 1l4 4-4 4" stroke="#222" fill="none"/></svg></span></div>
<div class="cat" style="left:686px;top:1100px;width:364px;height:310px;background:radial-gradient(ellipse 110px 60px at 190px 150px,#63c6be,rgba(99,198,190,0)),linear-gradient(175deg,#3c5734 0%,#6f7d58 22%,#cfc7bd 45%,#b4ab9f 75%,#6e5038 100%)" role="img" aria-label="Round turquoise resin side table on a rug"><span class="label">Molds</span><span class="go"><svg width="18" height="10"><path d="M0 5h16M12 1l4 4-4 4" stroke="#222" fill="none"/></svg></span></div>
<div class="cat" style="left:150px;top:1428px;width:362px;height:310px;background:linear-gradient(180deg,#eeedeb 0%,#dcd8d3 40%,#7a4f2e 48%,#9c6a44 55%,#d2ccc5 62%,#b8b1a9 100%)" role="img" aria-label="Wooden dining table with bench in a bright room"><span class="label">Wood</span><span class="go"><svg width="18" height="10"><path d="M0 5h16M12 1l4 4-4 4" stroke="#222" fill="none"/></svg></span></div>
<div class="cat" style="left:532px;top:1428px;width:518px;height:310px;background:radial-gradient(ellipse 50px 30px at 190px 90px,#d7c15a,rgba(215,193,90,0)),radial-gradient(ellipse 50px 30px at 420px 200px,#d7c15a,rgba(215,193,90,0)),linear-gradient(160deg,#6e7377,#b9bfc4 35%,#dfe3e6 55%,#7d858c 100%)" role="img" aria-label="Gloved hands spreading epoxy across a floor"><span class="label">Supplies</span><span class="go"><svg width="18" height="10"><path d="M0 5h16M12 1l4 4-4 4" stroke="#222" fill="none"/></svg></span></div>
<div class="cat" style="left:150px;top:1758px;width:900px;height:310px;background:radial-gradient(ellipse 380px 70px at 480px 130px,#8a5a32,rgba(138,90,50,0)),linear-gradient(172deg,#a9a8a6 0%,#8d8a86 20%,#5e4028 40%,#3d2b1d 58%,#2b2623 72%,#6a6764 100%)" role="img" aria-label="Walnut river table with clear resin on black legs"><span class="label">Furniture</span><span class="go"><svg width="18" height="10"><path d="M0 5h16M12 1l4 4-4 4" stroke="#222" fill="none"/></svg></span></div>

<div class="btn btn-light" style="left:524px;top:2110px;width:152px;height:38px">Shop All</div>

<!-- Classes -->
<div class="photo" style="left:0;top:2230px;width:1200px;height:478px;background:radial-gradient(ellipse 70px 40px at 520px 220px,#5a48b8,rgba(90,72,184,0)),radial-gradient(ellipse 50px 40px at 830px 270px,#3550c8,rgba(53,80,200,0)),radial-gradient(ellipse 300px 120px at 280px 170px,#dcdcdc,rgba(220,220,220,0)),linear-gradient(110deg,#9a9aa0 0%,#3a3b46 40%,#24252c 65%,#1a1a1f 100%)" role="img" aria-label="Hands in black gloves pouring purple resin into coaster molds"></div>
<div class="abs class-card">
  <h2>We Provide Classes<br>On How To Use Proxy</h2>
  <p class="para para-rule">Lorem Ipsum is simply dummy text of the printing and typesetting industry. Lorem Ipsum has been the industry's standard dummy text ever since the 1500s.</p>
  <div class="btn btn-dark" style="left:48px;top:248px;width:198px;height:36px">Reserve Now</div>
</div>

<!-- Products -->
<h2 class="abs section-title" style="top:2878px">Our Products</h2>
<div class="abs tabs"><span class="active">Brindle Epoxy</span><span>Molds</span><span>Wood</span><span>Supplies</span><span>Furniture</span></div>

<div class="product" style="left:150px;top:3048px"><div class="photo" role="img" aria-label="Two-part epoxy jugs with teal labels"></div><div class="name">Lorem Ipsum is simply</div><div class="price">$65.00</div><div class="btn btn-outline">Add To Cart</div></div>
<div class="product" style="left:380px;top:3040px"><div class="photo" style="height:242px" role="img" aria-label="Two-part epoxy jugs with teal labels"></div><div class="name">Lorem Ipsum is simply</div><div class="price">$65.00</div><div class="btn btn-light">Add To Cart</div></div>
<div class="product" style="left:608px;top:3048px"><div class="photo" role="img" aria-label="Two-part epoxy jugs with teal labels"></div><div class="name">Lorem Ipsum is simply</div><div class="price">$65.00</div><div class="btn btn-outline">Add To Cart</div></div>
<div class="product" style="left:838px;top:3048px"><div class="photo warm" role="img" aria-label="Two-part epoxy jugs with orange labels"></div><div class="name">Lorem Ipsum is simply</div><div class="price">$65.00</div><div class="btn btn-outline">Add To Cart</div></div>

<div class="btn btn-light" style="left:524px;top:3462px;width:152px;height:38px">View All</div>

<!-- Custom table -->
<div class="photo" style="left:0;top:3648px;width:1200px;height:394px;background:radial-gradient(ellipse 360px 80px at 330px 170px,#9a5e30,rgba(154,94,48,0)),radial-gradient(ellipse 180px 40px at 300px 170px,#1c1a18,rgba(28,26,24,0)),linear-gradient(160deg,#6c6a67 0%,#4a2e1a 25%,#5a3822 45%,#8a8784 62%,#9c9a97 100%)" role="img" aria-label="Live-edge walnut bench with black resin inlay"></div>
<h2 class="abs" style="left:650px;top:3752px;width:400px;text-align:right;font-size:38px;line-height:46px">Need A Custom<br>Table?</h2>
<p class="abs para" style="left:746px;top:3872px;width:304px;text-align:right;border-right:2px solid #fff;padding-right:12px;color:#eee">Lorem Ipsum is simply dummy text of the printing and typesetting industry. Lorem Ipsum has been the industry's</p>
<div class="btn btn-dark" style="left:894px;top:3950px;width:156px;height:38px">Shop Now</div>

<!-- About -->
<h2 class="abs" style="left:150px;top:4170px;font-size:40px">About Us</h2>
<div class="abs para para-rule" style="left:150px;top:4238px;width:440px">
  <p>Lorem Ipsum is simply dummy text of the printing and typesetting industry. Lorem Ipsum has been the industry's standard dummy text ever since the 1500s, when an unknown printer took a galley of type and scrambled it to make a type specimen book.</p>
  <p style="margin-top:14px">It was popularised in the 1960s with the release of Letraset sheets containing Lorem Ipsum passages, and more recently with desktop publishing software like Aldus PageMaker including versions of Lorem Ipsum.</p>
</div>
<div class="btn btn-light" style="left:150px;top:4456px;width:186px;height:36px">Explore More</div>
<div class="photo" style="left:668px;top:4130px;width:382px;height:400px;border-radius:6px;background:radial-gradient(ellipse 90px 70px at 210px 120px,#f2f2f2,rgba(242,242,242,0)),radial-gradient(ellipse 110px 60px at 170px 250px,#3a5588,rgba(58,85,136,0)),linear-gradient(170deg,#a7adb4,#8c929a 45%,#c9ccd0 80%,#dfe1e3)" role="img" aria-label="Worker in gloves applying epoxy to a floor"></div>
<div class="abs" style="left:624px;top:4406px;width:140px;height:140px;border-radius:50%;background:var(--dark);border:3px solid #fff;display:flex;flex-direction:column;align-items:center;justify-content:center;font-size:16px;font-weight:500;letter-spacing:1px;line-height:20px;text-transform:uppercase">Oakmere<span style="font-size:9px;letter-spacing:3px">Studio</span></div>

<!-- Footer -->
<div class="abs footer"></div>
<div class="abs footer-brand">Oakmere<span style="font-size:14px;letter-spacing:5px">Studio</span></div>
<div class="abs" style="left:150px;top:4940px;width:254px;height:36px;background:#fff;border-radius:3px;display:flex;align-items:center;justify-content:space-between;padding:0 12px;color:#777;font-size:10px">Your Mail
  <svg width="16" height="14"><path d="M1 7l14-6-5 12-2-5z" fill="#333"/></svg>
</div>
<div class="abs vline" style="left:482px;top:4720px;height:300px"></div>
<div class="abs vline" style="left:746px;top:4720px;height:300px"></div>
<div class="abs foot-head" style="left:560px;top:4718px">Useful Links</div>
<div class="abs foot-links" style="left:560px;top:4756px">Home<br>Brindle Epoxy<br>Molds<br>Wood<br>Supplies<br>Furniture<br>Education<br>About Us</div>
<div class="abs foot-head" style="left:824px;top:4718px">Contact</div>
<div class="abs" style="left:824px;top:4764px;display:flex;flex-direction:column;gap:34px">
  <div class="contact-row"><i><svg width="12" height="12"><path d="M2 1l3 0 1 3-2 1a7 7 0 0 0 3 3l1-2 3 1v3c-6 0-9-3-9-9z" fill="#222"/></svg></i>000-555-0142</div>
  <div class="contact-row"><i><svg width="12" height="10"><rect x="0.5" y="0.5" width="11" height="9" fill="none" stroke="#222"/><path d="M1 1l5 4 5-4" stroke="#222" fill="none"/></svg></i>info@oakmerestudio.com</div>
  <div class="contact-row"><i><svg width="10" height="13"><path d="M5 12S1 7 1 5a4 4 0 0 1 8 0c0 2-4 7-4 7z" fill="#222"/><circle cx="5" cy="5" r="1.5" fill="#fff"/></svg></i><span>218 Larch Avenue<br>Millbrook, CA 90000</span></div>
</div>
<div class="abs" style="left:828px;top:4986px;display:flex;gap:16px">
  <svg width="22" height="22"><circle cx="11" cy="11" r="11" fill="#fff"/></svg>
  <svg width="22" height="22"><circle cx="11" cy="11" r="11" fill="#fff"/></svg>
  <svg width="22" height="22"><circle cx="11" cy="11" r="11" fill="#fff"/></svg>
</div>
<div class="abs copy">Copyright © 2023 Oakmere Studio. All Rights Reserved.</div>

</body>
</html>
```